Business Stationery/templates
Business cards, email, powerpoint and word templates
Project: Business Stationery/templates
Business Stationery/templates - Consulting
Creative Brief
Professional
Gavin Brodell
518 Maple Ridge Rd Oakville, ON L6K 3R9
gbrodell@brodellms.ca
www.brodellms.ca
I am looking for business cards PLUS email, word and PowerPoint templates that incorporate the logo. The email template should not appear to have an attachment if there is only the logo and the text of the email.
I am passionate about working with Finance Functions that genuinely desire to increase the value that they are able to provide to the organization which they serve. From defining a Finance Function Strategy to delivering the vision, my commitment is to support you every step of the way.

```html
<!DOCTYPE html>
<html lang="en">
<head>
<meta charset="utf-8">
<title>Brodell Management Support – Business Cards</title>
<link href="https://fonts.googleapis.com/css2?family=Arimo:wght@400;700&display=swap" rel="stylesheet">
<style>
  :root {
    --page: #e9ebee;
    --white: #ffffff;
    --ink: #222831;
    --muted: #5a6270;
    --brand-blue: #1d63b8;
    --deep-blue: #142f86;
    --mid-blue: #2a5fd1;
    --brand-green: #3bb34a;
    --deep-green: #1f9a3c;
    --light-green: #7fd65a;
    --teal: #1c8fb5;
  }
  * { box-sizing: border-box; margin: 0; padding: 0; }
  html, body { width: 1200px; height: 1080px; overflow: hidden; }
  body {
    background: var(--page);
    font-family: "Arimo", Arial, sans-serif;
    position: relative;
    color: var(--ink);
  }
  .card {
    position: absolute;
    width: 470px;
    height: 270px;
    border-radius: 14px;
    overflow: hidden;
    box-shadow: 0 10px 24px rgba(0,0,0,.18);
  }

  /* front card */
  .card-front { left: 365px; top: 90px; background: var(--white); }
  .card-front .brand { position: absolute; left: 30px; top: 62px; width: 180px; }
  .card-front .divider {
    position: absolute; left: 222px; top: 40px; width: 2px; height: 138px;
    background: var(--ink);
  }
  .card-front .details { position: absolute; left: 240px; top: 40px; }
  .person-name { font-size: 26px; font-weight: 700; color: var(--ink); margin-bottom: 14px; }
  .address { font-size: 12px; line-height: 16px; color: var(--muted); margin-bottom: 4px; }
  .contact-line { display: flex; align-items: center; gap: 6px; font-size: 12px; line-height: 17px; color: var(--muted); }
  .contact-line svg { width: 11px; height: 11px; flex: none; }
  .card-front .band {
    position: absolute; left: 0; bottom: 0; width: 100%; height: 44px;
    background: linear-gradient(90deg, var(--deep-blue), var(--mid-blue) 60%, var(--deep-blue));
    border-top: 6px solid var(--brand-green);
    display: flex; align-items: center; justify-content: center;
  }
  .website { font-size: 12px; font-weight: 700; letter-spacing: 4px; color: var(--white); }

  /* brand block */
  .brand { display: flex; flex-direction: column; }
  .brand-row { display: flex; align-items: center; gap: 8px; }
  .brand-dot { width: 30px; height: 30px; border-radius: 50%; flex: none; }
  .brand-name { font-size: 15px; font-weight: 700; line-height: 16px; }
  .brand-tagline { font-size: 7px; margin-top: 4px; padding-left: 38px; }
  .card-front .brand-dot { background: var(--brand-blue); }
  .card-front .brand-name { color: var(--brand-blue); }
  .card-front .brand-tagline { color: var(--brand-green); }

  /* back cards */
  .card-back { padding: 28px 38px 0; }
  .card-back .brand { margin-left: 6px; }
  .statement {
    margin-top: 28px; font-size: 11.5px; line-height: 16px; text-align: center;
  }
  .card-back .website { position: absolute; left: 0; right: 0; bottom: 22px; text-align: center; }

  .card-blue {
    left: 115px; top: 385px;
    background: radial-gradient(ellipse at 70% 40%, #3f78e6 0%, var(--mid-blue) 35%, var(--deep-blue) 100%);
  }
  .card-blue .brand-dot { background: var(--white); }
  .card-blue .brand-name, .card-blue .statement { color: var(--white); }
  .card-blue .brand-tagline { color: #cfe0ff; }

  .card-white { left: 615px; top: 400px; background: var(--white); }
  .card-white .brand-dot { background: var(--brand-blue); }
  .card-white .brand-name { color: var(--brand-blue); }
  .card-white .brand-tagline { color: var(--brand-green); }
  .card-white .statement { color: var(--muted); }
  .card-white .website { color: var(--teal); }

  .card-green {
    left: 365px; top: 755px;
    background: radial-gradient(ellipse at 60% 40%, var(--light-green) 0%, var(--brand-green) 40%, var(--deep-green) 100%);
  }
  .card-green .brand-dot { background: var(--white); }
  .card-green .brand-name, .card-green .statement { color: var(--white); }
  .card-green .brand-tagline { color: #e6ffd9; }
</style>
</head>
<body>

<section class="card card-front">
  <div class="brand">
    <div class="brand-row">
      <span class="brand-dot"></span>
      <span class="brand-name">BRODELL<br>MANAGEMENT<br>SUPPORT</span>
    </div>
    <span class="brand-tagline">Adding value to your finance function</span>
  </div>
  <div class="divider"></div>
  <div class="details">
    <p class="person-name">Gavin Brodell</p>
    <p class="address">518 Maple Ridge Rd<br>Oakville, ON L6K 3R9</p>
    <p class="contact-line">
      <svg viewBox="0 0 12 12"><path d="M2 1h3l1 3-2 1a7 7 0 0 0 3 3l1-2 3 1v3c-6 0-9-3-9-9z" fill="var(--brand-blue)"/></svg>
      (416) 555-0148
    </p>
    <p class="contact-line">
      <svg viewBox="0 0 12 12"><rect x="0.5" y="2" width="11" height="8" fill="var(--brand-blue)"/><path d="M1 2.5l5 4 5-4" stroke="#fff" fill="none"/></svg>
      gbrodell@brodellms.ca
    </p>
    <p class="contact-line">
      <svg viewBox="0 0 12 12"><rect x="0.5" y="0.5" width="11" height="11" rx="2" fill="var(--brand-blue)"/></svg>
      Your profile
    </p>
  </div>
  <div class="band"><span class="website">www.brodellms.ca</span></div>
</section>

<section class="card card-back card-blue">
  <div class="brand">
    <div class="brand-row">
      <span class="brand-dot"></span>
      <span class="brand-name">BRODELL<br>MANAGEMENT<br>SUPPORT</span>
    </div>
    <span class="brand-tagline">Adding value to your finance function</span>
  </div>
  <p class="statement">I am passionate about working with Finance Functions that genuinely desire to increase the value that they are able to provide to the organization which they serve. From defining a Finance Function Strategy to delivering the vision, my commitment is to support you every step of the way.</p>
  <span class="website">www.brodellms.ca</span>
</section>

<section class="card card-back card-white">
  <div class="brand">
    <div class="brand-row">
      <span class="brand-dot"></span>
      <span class="brand-name">BRODELL<br>MANAGEMENT<br>SUPPORT</span>
    </div>
    <span class="brand-tagline">Adding value to your finance function</span>
  </div>
  <p class="statement">I am passionate about working with Finance Functions that genuinely desire to increase the value that they are able to provide to the organization which they serve. From defining a Finance Function Strategy to delivering the vision, my commitment is to support you every step of the way.</p>
  <span class="website">www.brodellms.ca</span>
</section>

<section class="card card-back card-green">
  <div class="brand">
    <div class="brand-row">
      <span class="brand-dot"></span>
      <span class="brand-name">BRODELL<br>MANAGEMENT<br>SUPPORT</span>
    </div>
    <span class="brand-tagline">Adding value to your finance function</span>
  </div>
  <p class="statement">I am passionate about working with Finance Functions that genuinely desire to increase the value that they are able to provide to the organization which they serve. From defining a Finance Function Strategy to delivering the vision, my commitment is to support you every step of the way.</p>
  <span class="website">www.brodellms.ca</span>
</section>

</body>
</html>
```